Banner Ad for Online e-commerce snack shop needs design for their Rivet Bundle Snack Box

We need 2 different size graphic designs that play off the same elements. The first will be a 1280px x 500px slide banner that will be used on the homepage of our website and the second will be an 800px x 800 px square ad that will be used on our box page (http://munchlooptreats.com/collections/taste-boxes) along with advertising on chatterlane. (which means copy only on 20%)

We are selling a snack box that includes 10 awesome, single-serve snacks from the great state of Colorado.

This design should play off the State of Colorado's flag or its icon. (similar to how the Juniper Parcel was done) It should also include in some form or fashion the 10 snacks or the box of snacks.

Please see the prior examples in the files uploaded. More can be seen at our site, munchlooptreats.com. The designs will need to be delivered to us as a PSD and a JPG file. Thank you for your time!

Industry/Entity Type

Advertising

Other font styles liked:
• Museo Slab 500 and/or Trebuchet MS

Requirements
Must have
• Rivet Bundle or Rivet Bundle Snack Box
• $19.95 or for only $19.95

```html
<!DOCTYPE html>
<html lang="en">
<head>
<meta charset="utf-8">
<title>Rivet Bundle Snack Box – Banner Set</title>
<link rel="stylesheet" href="https://fonts.googleapis.com/css2?family=Mulish:wght@400;500&family=PT+Sans:wght@700&display=swap">
<style>
  :root {
    --backdrop-light: #2c2c2c;
    --backdrop-dark: #101010;
    --flag-orange: #e04d27;
    --flag-green: #2e7a56;
    --divider-white: #ffffff;
    --text-white: #ffffff;
    --kraft-light: #c9a57a;
    --kraft-dark: #8b6b47;
    --snack-green: #4f9a3a;
    --snack-yellow: #e6cf58;
    --snack-blue: #2f5a9c;
  }
  * { margin: 0; padding: 0; box-sizing: border-box; }
  html, body { width: 1200px; height: 1000px; overflow: hidden; }
  body {
    position: relative;
    background: radial-gradient(ellipse at 50% 35%, var(--backdrop-light), var(--backdrop-dark) 80%);
    font-family: "Mulish", "Trebuchet MS", sans-serif;
    color: var(--text-white);
  }

  .slide-banner {
    position: absolute; left: 26px; top: 51px; width: 1147px; height: 447px;
    box-shadow: 6px 8px 14px rgba(0,0,0,.6);
    overflow: hidden;
  }
  .slide-banner .flag-field { position: absolute; inset: 0; }

  .snack-box-photo {
    position: absolute;
    border-radius: 6px;
    background:
      radial-gradient(circle at 30% 35%, var(--snack-green) 0 14%, transparent 15%),
      radial-gradient(circle at 62% 30%, var(--snack-yellow) 0 16%, transparent 17%),
      radial-gradient(circle at 82% 48%, var(--snack-blue) 0 12%, transparent 13%),
      linear-gradient(180deg, #d9c7a3 0%, #b89568 55%, var(--kraft-dark) 100%);
    opacity: .95;
  }
  .slide-banner .snack-box-photo { left: 16px; top: 48px; width: 455px; height: 366px; }

  .headline { text-align: center; text-shadow: 1px 2px 3px rgba(0,0,0,.45); font-weight: 400; }
  .headline .brand-name { display: block; line-height: 1; }
  .headline .product-type {
    display: flex; align-items: center; justify-content: center; line-height: 1;
  }
  .headline .product-type::before,
  .headline .product-type::after {
    content: ""; flex: 1; height: 3px; background: var(--text-white);
    box-shadow: 1px 2px 3px rgba(0,0,0,.35);
  }

  .price-callout {
    font-family: "PT Sans", "Trebuchet MS", sans-serif; font-weight: 700;
    text-align: center; text-shadow: 1px 2px 3px rgba(0,0,0,.45);
    letter-spacing: 1px;
  }

  .slide-banner .headline { position: absolute; left: 487px; top: 96px; width: 646px; }
  .slide-banner .brand-name { font-size: 66px; }
  .slide-banner .product-type { font-size: 42px; margin-top: 6px; }
  .slide-banner .product-type::before { margin-right: 12px; }
  .slide-banner .product-type::after { margin-left: 12px; }
  .slide-banner .price-callout {
    position: absolute; left: 560px; top: 272px; width: 540px;
    font-size: 60px; line-height: 58px;
  }

  .square-ad {
    position: absolute; left: 390px; top: 535px; width: 420px; height: 420px;
    background: var(--flag-orange);
    box-shadow: 6px 8px 14px rgba(0,0,0,.6);
    overflow: hidden;
  }
  .square-ad .title-band {
    position: absolute; left: 0; top: 0; width: 100%; height: 98px;
    background: var(--flag-green);
    border-bottom: 7px solid var(--divider-white);
  }
  .square-ad .headline { position: absolute; left: 50px; top: 24px; width: 325px; }
  .square-ad .brand-name { font-size: 32px; }
  .square-ad .product-type { font-size: 20px; margin-top: 2px; }
  .square-ad .product-type::before,
  .square-ad .product-type::after { height: 2px; }
  .square-ad .product-type::before { margin-right: 8px; }
  .square-ad .product-type::after { margin-left: 8px; }
  .square-ad .snack-box-photo { left: 78px; top: 125px; width: 246px; height: 220px; }
  .square-ad .price-band {
    position: absolute; left: 0; bottom: 0; width: 100%; height: 64px;
    background: var(--flag-green);
    border-top: 7px solid var(--divider-white);
    font-size: 32px; line-height: 56px;
  }
</style>
</head>
<body>
  <section class="slide-banner">
    <svg class="flag-field" width="1147" height="447" viewBox="0 0 1147 447" aria-hidden="true">
      <rect width="1147" height="447" fill="var(--flag-green)"/>
      <polygon points="0,0 392,0 570,447 0,447" fill="var(--flag-orange)"/>
      <polygon points="392,0 404,0 582,447 570,447" fill="var(--divider-white)"/>
    </svg>
    <div class="snack-box-photo" role="img" aria-label="Open kraft snack box filled with ten colourful single-serve snack packets"></div>
    <h1 class="headline">
      <span class="brand-name">Rivet Bundle</span>
      <span class="product-type">Snack Box</span>
    </h1>
    <p class="price-callout">FOR ONLY<br>$19.95</p>
  </section>

  <section class="square-ad">
    <div class="title-band"></div>
    <h2 class="headline">
      <span class="brand-name">Rivet Bundle</span>
      <span class="product-type">Snack Box</span>
    </h2>
    <div class="snack-box-photo" role="img" aria-label="Open kraft snack box filled with ten colourful single-serve snack packets"></div>
    <p class="price-callout price-band">FOR ONLY $19.95</p>
  </section>
</body>
</html>
```